I am a home builder and developer

I would like some sort of architectural design like a pencil type of drawing of a house but want it to be professional looking and two sided.

Simply I am a custom home builder and land developer. I would like a new design other than what I have now that's what I thought y'all did. I like mostly black maybe with an pencil type of drawing of a house. Like an architectural look.

Industry/Entity Type

Home Builder

```html
<!DOCTYPE html>
<html lang="en">
<head>
<meta charset="UTF-8">
<title>K &amp; L Casa Works – Business Card</title>
<link href="https://fonts.googleapis.com/css2?family=Orbitron:wght@500&display=swap" rel="stylesheet">
<style>
  :root {
    --paper: #ffffff;
    --card: #000000;
    --teal: #52c2c8;
  }
  html, body {
    margin: 0;
    padding: 0;
    width: 1077px;
    height: 1200px;
    overflow: hidden;
    background: var(--paper);
  }
  .sheet {
    position: relative;
    width: 1077px;
    height: 1200px;
  }
  .card {
    position: absolute;
    left: 4px;
    width: 1067px;
    height: 564px;
    background: var(--card);
    border-radius: 100px;
    font-family: "Orbitron", sans-serif;
    font-weight: 500;
    color: var(--teal);
    text-transform: uppercase;
  }
  .card--front { top: 4px; }
  .card--back { top: 629px; }
  .card__frame {
    position: absolute;
    inset: 22px;
    border: 3px dashed var(--teal);
    border-radius: 78px;
  }
  .brand {
    position: absolute;
    left: 0;
    right: 0;
    top: 180px;
    text-align: center;
    line-height: 1;
  }
  .brand__mark {
    display: block;
    width: 64px;
    height: 64px;
    margin: 0 auto 36px;
    background: var(--teal);
  }
  .brand__line {
    display: block;
    letter-spacing: 4px;
  }
  .brand__line--small { font-size: 64px; margin-bottom: 22px; }
  .brand__line--large { font-size: 84px; }
  .contact {
    position: absolute;
    left: 0;
    right: 0;
    top: 218px;
    text-align: center;
    font-size: 36px;
    line-height: 46px;
    letter-spacing: 2px;
  }
  .contact p { margin: 0; }
</style>
</head>
<body>
  <div class="sheet">
    <section class="card card--front">
      <div class="card__frame"></div>
      <div class="brand">
        <span class="brand__mark"></span>
        <span class="brand__line brand__line--small">K &amp; L</span>
        <span class="brand__line brand__line--large">Casa Works</span>
      </div>
    </section>

    <section class="card card--back">
      <div class="card__frame"></div>
      <div class="contact">
        <p class="contact__name">Owen Tallis</p>
        <p class="contact__phone">555.014.0392</p>
        <p class="contact__email">klcasaworks@mail.com</p>
      </div>
    </section>
  </div>
</body>
</html>
```